Anchored Willow Website

Would like a website designed for my fitness and nutrition coaching company Anchor Willow. I have a company logo and would like to keep the page layout clean and simple. Needs to look great on computer and mobile devices.

Target Market(s)

Target market is individuals looking to make changes in their health and nutrition with the help of an online coach.

Industry/Entity Type

Fitness

Number of Pages Required

2 page

Colors
3176b5
0355a3
85acd3
cedeed
f8fcfd
ffffff

Requirements
Must have
• The first page should have the company logo and name towards the top and below that client before and after photos scrolling or displaying in some manner. Also would like a section that states services offered and a section about myself since I am the primary coach for clients.

```html
<!DOCTYPE html>
<html lang="en">
<head>
<meta charset="utf-8">
<title>Anchored Willow – Fitness &amp; Nutrition Coaching</title>
<link rel="stylesheet" href="https://fonts.googleapis.com/css2?family=Open+Sans:wght@400;600;700;800&display=swap">
<style>
:root{
  --blue:#0355a3;
  --blue-mid:#3176b5;
  --blue-light:#85acd3;
  --blue-pale:#cedeed;
  --bright:#3d93de;
  --navy:#132235;
  --ink:#1c1c1c;
  --grey:#666;
  --white:#ffffff;
  --footer:#2f6cb2;
}
*{margin:0;padding:0;box-sizing:border-box}
html,body{width:1200px;height:4196px;overflow:hidden;background:var(--white)}
body{font-family:"Open Sans",Arial,sans-serif;color:var(--ink);position:relative}
section,header,footer{position:absolute;left:0;width:1200px}
.abs{position:absolute}
.section-title{position:absolute;left:0;width:1200px;text-align:center;font-weight:700;font-size:19px;letter-spacing:.5px}
.section-title::after{content:"";display:block;width:46px;height:3px;background:var(--blue);margin:16px auto 0}

/* header */
.site-header{top:0;height:117px;background:var(--white)}
.brand{left:131px;top:30px;display:flex;align-items:center;gap:12px}
.brand-mark{width:34px;height:34px;background:var(--blue)}
.brand-name{font-size:22px;font-weight:700;color:var(--blue);text-transform:uppercase;letter-spacing:.5px}
.call{left:757px;top:22px;display:flex;gap:10px;align-items:center}
.call-icon{width:30px;height:30px;border-radius:50%;background:var(--blue);display:flex;align-items:center;justify-content:center}
.call small{display:block;font-size:10px;font-weight:700}
.call strong{display:block;font-size:19px;color:var(--blue-mid);font-weight:600;line-height:1.1}
.search{left:945px;top:24px;width:126px;height:32px;border:1px solid #ccc;font-size:9px;color:#999;padding:10px 10px;display:flex;justify-content:space-between}
.nav{left:531px;top:76px;display:flex;gap:0;font-size:11px;font-weight:600}
.nav a{color:var(--ink);text-decoration:none;padding:7px 15px}
.nav a.active{background:var(--blue);color:var(--white)}

/* hero */
.hero{top:117px;height:596px;background:linear-gradient(100deg,#3c4650 0%,#7c8a85 35%,#a9b6a8 55%,#6f7d78 80%,#3a4350 100%)}
.hero-title{left:649px;top:270px;font-size:56px;font-weight:700;line-height:1;color:var(--bright);text-transform:uppercase}
.hero-list{left:649px;top:400px;list-style:none;color:var(--white);font-weight:700;font-size:18px}
.hero-list li{margin-bottom:13px;display:flex;align-items:center;gap:12px}
.hero-list li::before{content:"";border-left:9px solid var(--bright);border-top:6px solid transparent;border-bottom:6px solid transparent}
.dots{left:555px;top:541px;display:flex;gap:10px}
.dots i{width:9px;height:9px;border-radius:50%;background:rgba(255,255,255,.6)}
.dots i:first-child{background:var(--white)}

/* services */
.services{top:713px;height:484px}
.service{position:absolute;top:135px;width:220px;text-align:center}
.diamond{width:122px;height:122px;background:var(--blue);transform:rotate(45deg);margin:26px auto 0;display:flex;align-items:center;justify-content:center}
.diamond svg{transform:rotate(-45deg)}
.service h3{font-size:13px;font-weight:600;margin-top:66px;text-transform:uppercase}
.service p{font-size:10.5px;color:var(--grey);line-height:1.45;margin-top:12px;padding:0 4px}

/* welcome */
.welcome{top:1197px;height:495px;background:linear-gradient(90deg,#0f1d2e 0%,#16283d 55%,#0f1b2b 100%)}
.welcome-photo{left:643px;top:0;width:280px;height:495px;background:linear-gradient(180deg,#2a3a4d,#45566a 50%,#1b2a3b)}
.welcome h2{left:154px;top:70px;color:var(--white);font-size:19px;font-weight:700}
.welcome h2::after{content:"";display:block;width:46px;height:3px;background:var(--blue-mid);margin-top:16px}
.welcome .intro{left:154px;top:140px;width:445px;color:#c8d1db;font-size:11px;line-height:1.7}
.feature{left:154px;display:flex;align-items:center;gap:22px;color:var(--white)}
.feature-icon{width:64px;height:64px;border-radius:50%;background:var(--blue);display:flex;align-items:center;justify-content:center}
.feature h4{font-size:13px;font-weight:700}
.feature p{font-size:10.5px;color:#b8c3cf;margin-top:4px}

/* before after */
.results{top:1692px;height:504px}
.result{position:absolute;top:148px;width:224px;text-align:center}
.result .photo{height:244px}
.result h4{font-size:12px;font-weight:700;color:var(--blue);margin-top:18px}
.result p{font-size:10.5px;color:var(--grey);margin-top:3px}
.arrow{position:absolute;top:258px}

/* coaches */
.coaches{top:2196px;height:470px;background:var(--blue);color:var(--white)}
.coaches .section-title::after{background:var(--white)}
.coach{position:absolute;top:156px;width:210px}
.coach .photo{height:193px}
.coach h4{font-size:12px;font-weight:700;margin-top:18px}
.coach p{font-size:10px;line-height:1.4;width:160px;margin-top:4px;color:var(--blue-pale)}
.coach svg{position:absolute;right:14px;top:224px}

/* nutrition */
.nutrition{top:2666px;height:537px;background:linear-gradient(90deg,#c9dbe6 0%,#dbe6ea 40%,#a9bfcf 60%,#8fa8b4 100%)}
.nutrition h2{left:204px;top:88px;font-size:36px;font-weight:700;line-height:1.05;color:var(--blue);text-transform:uppercase}
.nutrition p{left:204px;top:184px;width:320px;font-size:12px;line-height:1.55;color:#333}
.btn{display:inline-block;background:var(--blue);color:var(--white);font-size:10.5px;font-weight:700;text-transform:uppercase;padding:12px 22px}
.nutrition .btn{position:absolute;left:210px;top:268px}

/* blog */
.blog{top:3203px;height:615px}
.post{position:absolute;top:153px;width:294px}
.post .photo{height:235px}
.post h4{font-size:13px;font-weight:700;line-height:1.45;margin-top:28px;text-transform:uppercase}
.post p{font-size:11.5px;color:var(--grey);line-height:1.5;margin-top:12px;width:260px}
.post .btn{margin-top:16px;padding:9px 20px;font-size:10px}

/* footer */
.site-footer{top:3818px;height:378px;background:var(--footer);color:var(--white)}
.footer-brand{left:131px;top:110px;display:flex;align-items:center;gap:10px}
.footer-brand .brand-mark{background:var(--white);width:26px;height:26px}
.footer-brand span{font-size:18px;font-weight:700;text-transform:uppercase}
.col h5{font-size:11px;font-weight:700;text-transform:uppercase;margin-bottom:18px}
.contact-list{list-style:none;font-size:10px;line-height:1.45}
.contact-list li{display:flex;gap:14px;margin-bottom:22px}
.menu-list{list-style:none;font-size:10px;line-height:1.55;text-transform:uppercase}
.email{width:248px;height:40px;background:var(--white);color:#999;font-size:11px;padding:12px 14px;display:flex;gap:10px;align-items:center}
.subscribe{margin-top:16px;padding:10px 16px;background:var(--blue);font-size:10px;font-weight:700;display:inline-block;text-transform:uppercase}
.rule{left:131px;top:285px;width:938px;height:1px;background:rgba(255,255,255,.3)}
.follow{left:131px;top:302px;display:flex;align-items:center;gap:12px;font-size:10px;font-weight:700}
.follow span{margin-right:24px}
.follow i{width:26px;height:26px;border-radius:50%;background:var(--blue)}
.copyright{right:131px;top:312px;font-size:10px}
</style>
</head>
<body>

<header class="site-header">
  <div class="abs brand"><span class="brand-mark"></span><span class="brand-name">Anchored Willow</span></div>
  <div class="abs call">
    <span class="call-icon"><svg width="14" height="14" viewBox="0 0 24 24"><path fill="#fff" d="M6.6 10.8a15 15 0 0 0 6.6 6.6l2.2-2.2c.3-.3.7-.4 1-.2 1.1.4 2.3.6 3.6.6.6 0 1 .4 1 1V20c0 .6-.4 1-1 1A17 17 0 0 1 3 4c0-.6.4-1 1-1h3.5c.6 0 1 .4 1 1 0 1.3.2 2.5.6 3.6.1.3 0 .7-.2 1z"/></svg></span>
    <div><small>CALL US</small><strong>555.014.2290</strong></div>
  </div>
  <div class="abs search"><span>SEARCH</span><svg width="10" height="10" viewBox="0 0 10 10"><circle cx="4" cy="4" r="3" fill="none" stroke="#555" stroke-width="1.3"/><path d="M6.3 6.3 9 9" stroke="#555" stroke-width="1.3"/></svg></div>
  <nav class="abs nav">
    <a class="active" href="#">HOME</a><a href="#">ABOUT US</a><a href="#">SERVICES</a><a href="#">FITNESS</a><a href="#">NUTRITION</a><a href="#">BLOG</a><a href="#">CONTACT US</a>
  </nav>
</header>

<section class="hero" role="img" aria-label="Athlete lifting a barbell overhead in a smoky gym">
  <h1 class="abs hero-title">Fitness<br>Coaching</h1>
  <ul class="abs hero-list"><li>EAT WELL</li><li>LOVE YOUR BODY</li><li>LIVE HEALTHY</li></ul>
  <div class="abs dots"><i></i><i></i><i></i><i></i><i></i></div>
</section>

<section class="services">
  <h2 class="section-title" style="top:52px">OUR SERVICES</h2>
  <div class="service" style="left:119px">
    <div class="diamond"><svg width="46" height="46" viewBox="0 0 46 46"><rect x="4" y="17" width="6" height="12" fill="#fff"/><rect x="36" y="17" width="6" height="12" fill="#fff"/><rect x="10" y="21" width="26" height="4" fill="#fff"/><rect x="0" y="20" width="4" height="6" fill="#fff"/><rect x="42" y="20" width="4" height="6" fill="#fff"/></svg></div>
    <h3>Coaching</h3><p>Lorem Ipsum is simply dummy text of the printing and typesetting industry. Lorem Ipsum has been.</p>
  </div>
  <div class="service" style="left:363px">
    <div class="diamond"><svg width="46" height="46" viewBox="0 0 46 46"><circle cx="23" cy="27" r="15" fill="#fff"/><path d="M23 12c2-6 7-7 9-6-1 4-5 6-9 6z" fill="#fff"/></svg></div>
    <h3>Nutrition Programs</h3><p>Lorem Ipsum is simply dummy text of the printing and typesetting industry. Lorem Ipsum has been.</p>
  </div>
  <div class="service" style="left:606px">
    <div class="diamond"><svg width="46" height="46" viewBox="0 0 46 46"><rect x="9" y="6" width="28" height="36" rx="2" fill="none" stroke="#fff" stroke-width="3"/><path d="M15 17h16M15 24h16M15 31h10" stroke="#fff" stroke-width="3"/></svg></div>
    <h3>Fitness Plan</h3><p>Lorem Ipsum is simply dummy text of the printing and typesetting industry. Lorem Ipsum has been.</p>
  </div>
  <div class="service" style="left:861px">
    <div class="diamond"><svg width="40" height="40" viewBox="0 0 24 24"><path fill="#fff" d="M6.6 10.8a15 15 0 0 0 6.6 6.6l2.2-2.2c.3-.3.7-.4 1-.2 1.1.4 2.3.6 3.6.6.6 0 1 .4 1 1V20c0 .6-.4 1-1 1A17 17 0 0 1 3 4c0-.6.4-1 1-1h3.5c.6 0 1 .4 1 1 0 1.3.2 2.5.6 3.6.1.3 0 .7-.2 1z"/></svg></div>
    <h3>Get a Consultation</h3><p>Lorem Ipsum is simply dummy text of the printing and typesetting industry. Lorem Ipsum has been.</p>
  </div>
</section>

<section class="welcome">
  <div class="abs welcome-photo" role="img" aria-label="Athlete training on gymnastic rings"></div>
  <h2 class="abs">WELCOME TO OUR SITE</h2>
  <p class="abs intro">There are many variations of passages of Lorem Ipsum available, but the majority have suffered alteration in some form, by injected humour, or randomised words which don't look even slightly believable. If you are going to use a passage of Lorem Ipsum you need to be sure.</p>
  <div class="abs feature" style="top:259px">
    <span class="feature-icon"><svg width="30" height="16" viewBox="0 0 30 16"><rect x="2" y="2" width="5" height="12" fill="#fff"/><rect x="23" y="2" width="5" height="12" fill="#fff"/><rect x="7" y="6" width="16" height="4" fill="#fff"/></svg></span>
    <div><h4>TRAINING</h4><p>There are many variations of passages</p></div>
  </div>
  <div class="abs feature" style="top:351px">
    <span class="feature-icon"><svg width="26" height="26" viewBox="0 0 26 26"><circle cx="9" cy="8" r="4" fill="#fff"/><circle cx="18" cy="9" r="3" fill="#fff"/><path d="M2 22c0-5 3-8 7-8s7 3 7 8zM15 22c0-3 1-6 3-7 3 0 6 2 6 7z" fill="#fff"/></svg></span>
    <div><h4>BEST TEAM</h4><p>There are many variations of passages</p></div>
  </div>
</section>

<section class="results">
  <h2 class="section-title" style="top:52px">BEFORE &amp; AFTER</h2>
  <svg class="arrow" style="left:78px" width="12" height="22" viewBox="0 0 12 22"><path d="M10 2 2 11l8 9" fill="none" stroke="#999" stroke-width="2"/></svg>
  <svg class="arrow" style="left:1108px" width="12" height="22" viewBox="0 0 12 22"><path d="M2 2l8 9-8 9" fill="none" stroke="#999" stroke-width="2"/></svg>
  <div class="result" style="left:134px"><div class="photo" role="img" aria-label="Before and after photo of a client's waist" style="background:linear-gradient(90deg,#d8c3b4,#ece4dc)"></div><h4>LOREM IPSUM</h4><p>There are many variations</p></div>
  <div class="result" style="left:372px"><div class="photo" role="img" aria-label="Before and after side profile of a client" style="background:linear-gradient(90deg,#cdb6a4,#e6dfd8)"></div><h4>LOREM IPSUM</h4><p>There are many variations</p></div>
  <div class="result" style="left:610px"><div class="photo" role="img" aria-label="Before and after torso of a male client" style="background:linear-gradient(90deg,#8a6d5a,#5d4a3e)"></div><h4>LOREM IPSUM</h4><p>There are many variations</p></div>
  <div class="result" style="left:848px"><div class="photo" role="img" aria-label="Before and after side view of a client" style="background:linear-gradient(90deg,#9aa0a0,#b7b2ad)"></div><h4>LOREM IPSUM</h4><p>There are many variations</p></div>
</section>

<section class="coaches">
  <h2 class="section-title" style="top:52px">MEET COACHES</h2>
  <div class="coach" style="left:134px"><div class="photo" role="img" aria-label="Coach portrait in a gym" style="background:linear-gradient(135deg,#5a3d36,#2e2624)"></div><h4>ALVAREZ</h4><p>It is a long established fact that a reader</p><svg width="10" height="16" viewBox="0 0 10 16"><path d="M2 2l6 6-6 6" fill="none" stroke="#fff" stroke-width="2"/></svg></div>
  <div class="coach" style="left:372px"><div class="photo" role="img" aria-label="Coach portrait" style="background:linear-gradient(135deg,#8a7a6e,#3f3633)"></div><h4>WHITMAN</h4><p>It is a long established fact that a reader</p><svg width="10" height="16" viewBox="0 0 10 16"><path d="M2 2l6 6-6 6" fill="none" stroke="#fff" stroke-width="2"/></svg></div>
  <div class="coach" style="left:610px"><div class="photo" role="img" aria-label="Coach portrait in a gym" style="background:linear-gradient(135deg,#6b5448,#33302f)"></div><h4>SUTTON</h4><p>It is a long established fact that a reader</p><svg width="10" height="16" viewBox="0 0 10 16"><path d="M2 2l6 6-6 6" fill="none" stroke="#fff" stroke-width="2"/></svg></div>
  <div class="coach" style="left:848px"><div class="photo" role="img" aria-label="Coach portrait" style="background:linear-gradient(135deg,#a78d78,#5f5048)"></div><h4>HARLOW</h4><p>It is a long established fact that a reader</p><svg width="10" height="16" viewBox="0 0 10 16"><path d="M2 2l6 6-6 6" fill="none" stroke="#fff" stroke-width="2"/></svg></div>
</section>

<section class="nutrition" role="img" aria-label="Woman drinking from a water bottle outdoors by a lake">
  <h2 class="abs">Nutrition<br>Coaching</h2>
  <p class="abs">There are many variations of passages of Lorem Ipsum available, but the majority have suffered alteration in some form, by injected humour, or randomised words which don't look.</p>
  <a class="btn" href="#">Read more</a>
</section>

<section class="blog">
  <h2 class="section-title" style="top:52px">LATEST BLOG</h2>
  <article class="post" style="left:134px"><div class="photo" role="img" aria-label="People training with barbells in a gym" style="background:linear-gradient(135deg,#5c5148,#2c2724)"></div><h4>It is a long established fact<br>that a reader</h4><p>There are many variations of passages of Lorem Ipsum available.</p><a class="btn" href="#">Read more</a></article>
  <article class="post" style="left:459px"><div class="photo" role="img" aria-label="Bowl of oats with berries" style="background:linear-gradient(135deg,#cdb79a,#6d5546)"></div><h4>It is a long established fact<br>that a reader</h4><p>There are many variations of passages of Lorem Ipsum available.</p><a class="btn" href="#">Read more</a></article>
  <article class="post" style="left:775px"><div class="photo" role="img" aria-label="Athletes exercising in a dark gym" style="background:linear-gradient(135deg,#4a4440,#1f1d1c)"></div><h4>It is a long established fact<br>that a reader</h4><p>There are many variations of passages of Lorem Ipsum available.</p><a class="btn" href="#">Read more</a></article>
</section>

<footer class="site-footer">
  <div class="abs footer-brand"><span class="brand-mark"></span><span>Anchored Willow</span></div>
  <div class="abs col" style="left:394px;top:56px">
    <h5>Contact us</h5>
    <ul class="contact-list">
      <li><svg width="10" height="12" viewBox="0 0 10 12"><path d="M5 0a4 4 0 0 1 4 4c0 3-4 8-4 8S1 7 1 4a4 4 0 0 1 4-4z" fill="#fff"/></svg><span>14 Harbor Lane<br>Lake Crest, SD 57001</span></li>
      <li><svg width="10" height="10" viewBox="0 0 24 24"><path fill="#fff" d="M6.6 10.8a15 15 0 0 0 6.6 6.6l2.2-2.2c.3-.3.7-.4 1-.2 1.1.4 2.3.6 3.6.6.6 0 1 .4 1 1V20c0 .6-.4 1-1 1A17 17 0 0 1 3 4c0-.6.4-1 1-1h3.5c.6 0 1 .4 1 1 0 1.3.2 2.5.6 3.6.1.3 0 .7-.2 1z"/></svg><span>555-014-2290</span></li>
      <li><svg width="11" height="9" viewBox="0 0 11 9"><rect x=".5" y=".5" width="10" height="8" fill="none" stroke="#fff"/><path d="M.5.5 5.5 5l5-4.5" fill="none" stroke="#fff"/></svg><span>info@anchoredwillow.com</span></li>
    </ul>
  </div>
  <div class="abs col" style="left:643px;top:56px">
    <h5>Menu</h5>
    <ul class="menu-list"><li>Home</li><li>About us</li><li>Services</li><li>Fitness</li><li>Nutrition</li><li>Blog</li><li>Contact us</li></ul>
  </div>
  <div class="abs col" style="left:820px;top:56px">
    <h5>Subscribe for updates</h5>
    <div class="email"><svg width="11" height="9" viewBox="0 0 11 9"><rect x=".5" y=".5" width="10" height="8" fill="none" stroke="#999"/><path d="M.5.5 5.5 5l5-4.5" fill="none" stroke="#999"/></svg>E-mail id</div>
    <span class="subscribe">Subscribe</span>
  </div>
  <div class="abs rule"></div>
  <div class="abs follow"><span>FOLLOW US</span><i></i><i></i><i></i><i></i><i></i></div>
  <div class="abs copyright">Copyrights © 2017 All Rights Reserved</div>
</footer>

</body>
</html>
```